KickHarbor.com Website

We need a dynamic, vibrant and modern design for our new website.

KickHarbor will bridge the generational gap between young and old by bringing together footballers from different generations to play with and against each other, whilst giving fans a unique opportunity to watch them.

Old memories will be passed from parents to children or from grandparents to grandchildren, whilst new memories are created and shared.

The website will provide fans from all over the world with exclusive content, merchandise, tickets and forums on which to exchange their stories, experiences and opinions.

The winning website design needs to be as unique as the product whilst and provide the perfect platform from which to reach, attract and keep as many fans as possible.

Target Market(s)

Worldwide football fans across generations and from different teams.

Number of Pages Required

3 page

Requirements
Must have
• Included KickHarbor logo design as attached. The colours from the logo should also be incorporated throughout the website where possible.
• Home Page, Merchandise Page, Teams Page - screen shots attached for information.
Should not have
• Any reference to or pictures of American Football

```html
<!DOCTYPE html>
<html lang="en">
<head>
<meta charset="utf-8">
<title>KickHarbor.com – Latest News</title>
<link rel="stylesheet" href="https://fonts.googleapis.com/css2?family=Open+Sans:wght@400;600;700&display=swap">
<style>
:root{
  --blue:#1a8ad4;
  --red:#e3301c;
  --green:#4aa511;
  --green-dark:#3a8e0c;
  --ink:#333;
  --muted:#666;
  --line:#dcdcdc;
  --footer:#1b1b1b;
}
*{box-sizing:border-box;margin:0;padding:0}
html,body{width:969px;height:1200px;overflow:hidden;background:#fff}
body{position:relative;font-family:"Open Sans",Arial,sans-serif;color:var(--ink)}
.abs{position:absolute}
.topbar{left:0;top:0;width:969px;height:3px;background:linear-gradient(90deg,var(--blue) 0 33%,var(--red) 33% 66.5%,var(--green) 66.5%)}
.brand{left:130px;top:40px;display:flex;align-items:center;gap:8px;font-size:22px;font-weight:700;color:var(--blue)}
.brand i{width:22px;height:22px;background:var(--red);display:block}
.btn{top:18px;height:31px;color:#fff;font-size:9.5px;font-weight:700;display:flex;align-items:center;justify-content:center;border-radius:2px}
.btn-login{left:707px;width:63px;background:var(--red)}
.btn-signup{left:774px;width:64px;background:var(--blue)}
.nav{top:77px;left:0;font-size:10.5px;font-weight:600;color:#222;text-transform:uppercase}
.nav span{position:absolute;white-space:nowrap;top:0}
.nav .active{color:var(--green)}
.nav-marker{left:425px;top:104px;width:0;height:0;border-left:7px solid transparent;border-right:7px solid transparent;border-bottom:6px solid var(--green)}
.hero{left:0;top:110px;width:969px;height:299px;background:radial-gradient(ellipse at 50% 55%,#3f6e3a 0%,#1f3d23 45%,#0d1a12 100%)}
.hero h1{position:absolute;left:0;right:0;top:130px;text-align:center;color:#fff;font-size:32px;font-weight:700;letter-spacing:-.5px}
.section-title{font-size:14.5px;font-weight:700;color:#3a3a3a;text-transform:uppercase;display:flex;align-items:center;letter-spacing:-.2px}
.section-title::after{content:"";width:7px;height:7px;border-radius:50%;background:var(--blue);margin-left:5px;flex:none}
.rule{height:1px;background:var(--line)}
.copy{font-size:8.8px;line-height:15.2px;color:var(--muted);text-align:justify}
.match-box{left:130px;top:526px;width:336px;height:141px;border:1px solid #ddd}
.crest{top:14px;width:147px;height:113px;background:linear-gradient(135deg,#fff,#e3e3e3);border:1px solid #ccc;display:flex;align-items:center;justify-content:center;font-size:12px;font-weight:700;color:var(--red);z-index:1}
.crest-home{left:12px;padding-right:14px}
.crest-away{left:175px;padding-left:14px}
.vs{left:146px;top:48px;width:43px;height:43px;border-radius:50%;background:var(--green);color:#fff;font-size:17px;display:flex;align-items:center;justify-content:center;z-index:2}
.cta-title{left:505px;top:462px;font-size:12.2px;color:var(--blue);font-weight:400}
.count{top:555px;width:79px;height:62px;border:1px solid #d8d8d8;background:#f5f5f5;text-align:center}
.count b{display:block;font-size:21px;margin-top:6px;color:#333}
.count span{font-size:11px;color:var(--green);text-transform:uppercase}
.buy{left:503px;top:631px;width:164px;height:33px;background:linear-gradient(var(--green),var(--green-dark));color:#fff;font-size:10.5px;font-weight:700;display:flex;align-items:center;justify-content:center;gap:6px;border-radius:2px}
.item-thumb{width:104px;height:87px;border:3px solid #fff;box-shadow:0 0 0 1px #ddd}
.item-title{font-size:13.5px;font-weight:700}
.meta{font-size:8.8px;color:var(--green)}
.fan-logo{width:105px;height:87px;border:1px solid #ddd;display:flex;align-items:center;justify-content:center;font-size:10.5px;font-weight:700}
.more{font-size:8.8px;font-weight:700;color:var(--green)}
.footer{left:0;top:1141px;width:969px;height:59px;background:var(--footer)}
.social{top:16px;width:26px;height:26px;border:2px solid #fff;border-radius:50%}
.legal{right:130px;top:23px;font-size:8.6px;color:#ccc}
</style>
</head>
<body>
<div class="abs topbar"></div>

<header>
  <div class="abs brand"><i></i>KickHarbor</div>
  <a class="abs btn btn-login">LOGIN</a>
  <a class="abs btn btn-signup">SIGN UP</a>
  <nav class="abs nav">
    <span style="left:338px">Home</span>
    <span style="left:399px" class="active">Latest News</span>
    <span style="left:496px">Teams</span>
    <span style="left:558px">Merchandise</span>
    <span style="left:661px">Competitions</span>
    <span style="left:766px">Tickets</span>
    <svg style="position:absolute;left:828px;top:2px" width="11" height="11" viewBox="0 0 11 11"><circle cx="4.5" cy="4.5" r="3.3" fill="none" stroke="#1a8ad4" stroke-width="1.6"/><line x1="7" y1="7" x2="10" y2="10" stroke="#1a8ad4" stroke-width="1.8"/></svg>
  </nav>
  <div class="abs nav-marker"></div>
</header>

<section class="abs hero" role="img" aria-label="Two footballers, one in blue holding a ball, one in red juggling a ball, on a floodlit stadium pitch">
  <h1>LATEST NEWS</h1>
</section>

<section>
  <h2 class="abs section-title" style="left:130px;top:429px">The Next Match</h2>
  <div class="abs rule" style="left:274px;top:439px;width:564px"></div>
  <p class="abs copy" style="left:130px;top:462px;width:336px">Sed ut perspiciatis unde omnis iste natus error sit voluptatem accusantium doloremque laudantium, totam rem aperiam, eaque ipsa quae ab illo inventore veritatis et quasi architecto beatae vitae dicta sunt explicabo.</p>
  <div class="abs match-box">
    <div class="abs crest crest-home">Redport FC</div>
    <div class="abs crest crest-away">Alpenstadt FC</div>
    <div class="abs vs">VS</div>
  </div>

  <h3 class="abs cta-title">Don’t miis the the opportunity to see this Epic game live</h3>
  <p class="abs copy" style="left:505px;top:491px;width:335px">Sed ut perspiciatis unde omnis iste natus error sit voluptatem accusantium doloremque laudantium, totam rem aperiam, eaque ipsa quae ab illo inventore veritatis et quasi architecto beatae vitae dicta sunt explicabo.</p>
  <div class="abs count" style="left:503px"><b>8</b><span>Days</span></div>
  <div class="abs count" style="left:588px"><b>20</b><span>Hours</span></div>
  <div class="abs count" style="left:673px"><b>13</b><span>Minutes</span></div>
  <div class="abs count" style="left:758px;width:80px"><b>47</b><span>Seconds</span></div>
  <a class="abs buy">BUY THIS TICKETS NOW
    <svg width="11" height="11" viewBox="0 0 11 11"><path d="M1 6 L6 1 L10 1 L10 5 L5 10 Z" fill="#fff"/><circle cx="8" cy="3" r="1" fill="#3a8e0c"/></svg>
  </a>
</section>

<div class="abs rule" style="left:130px;top:718px;width:708px"></div>
<div class="abs rule" style="left:130px;top:722px;width:708px"></div>
<svg class="abs" style="left:462px;top:698px" width="48" height="48" viewBox="0 0 48 48">
  <circle cx="24" cy="24" r="22.5" fill="#fff" stroke="#111" stroke-width="2"/>
  <polygon points="24,16 31,21 28,29 20,29 17,21" fill="#111"/>
</svg>

<section>
  <h2 class="abs section-title" style="left:130px;top:773px">The Latest News</h2>
  <div class="abs rule" style="left:270px;top:783px;width:193px"></div>

  <div class="abs item-thumb" style="left:130px;top:817px;background:linear-gradient(135deg,#c9558a,#f0a030 60%,#f4d25a)" role="img" aria-label="Football on grass at sunset"></div>
  <h3 class="abs item-title" style="left:251px;top:814px;color:var(--blue)">Sed ut perspiciatis unde omn</h3>
  <p class="abs copy" style="left:251px;top:836px;width:215px">Sed ut perspiciatis unde omnis iste natus error sit voluptatem accusantium doloremque laudantium, totam rem aperiam, eaque ipsa quae ab illo</p>
  <div class="abs meta" style="left:251px;top:886px">▢ Feb 05 2016 &nbsp;● Comments</div>

  <div class="abs item-thumb" style="left:130px;top:917px;background:linear-gradient(#8fae6a,#5e8c38)" role="img" aria-label="Two young players chasing a ball on a pitch"></div>
  <h3 class="abs item-title" style="left:251px;top:914px;color:var(--red)">Sed ut perspiciatis unde omn</h3>
  <p class="abs copy" style="left:251px;top:935px;width:215px">Sed ut perspiciatis unde omnis iste natus error sit voluptatem accusantium doloremque laudantium, totam rem aperiam, eaque ipsa quae ab illo</p>
  <div class="abs meta" style="left:251px;top:985px">▢ Feb 05 2016 &nbsp;● Comments</div>

  <div class="abs item-thumb" style="left:130px;top:1021px;background:linear-gradient(#3a3a44,#6b5a48 60%,#4f7a36)" role="img" aria-label="Players contesting the ball at a night match"></div>
  <h3 class="abs item-title" style="left:251px;top:1017px;color:var(--green)">Sed ut perspiciatis unde omn</h3>
  <p class="abs copy" style="left:251px;top:1039px;width:215px">Sed ut perspiciatis unde omnis iste natus error sit voluptatem accusantium doloremque laudantium, totam rem aperiam, eaque ipsa quae ab illo</p>
  <div class="abs meta" style="left:251px;top:1089px">▢ Feb 05 2016 &nbsp;● Comments</div>
</section>

<section>
  <h2 class="abs section-title" style="left:506px;top:773px">Most Popular Fanclubs</h2>
  <div class="abs rule" style="left:722px;top:783px;width:114px"></div>

  <div class="abs fan-logo" style="left:503px;top:817px;color:var(--blue)">KickHarbor</div>
  <h3 class="abs item-title" style="left:625px;top:814px;color:var(--red)">Sed ut perspiciatis unde omn</h3>
  <p class="abs copy" style="left:625px;top:836px;width:214px">Sed ut perspiciatis unde omnis iste natus error sit voluptatem accusantium doloremque laudantium, totam rem aperiam, eaque ipsa quae ab illo</p>
  <div class="abs more" style="left:625px;top:886px">⊕ READ MORE</div>

  <div class="abs fan-logo" style="left:503px;top:918px;color:var(--red)">Alpenstadt FC</div>
  <h3 class="abs item-title" style="left:625px;top:915px;color:var(--green)">Sed ut perspiciatis unde omn</h3>
  <p class="abs copy" style="left:625px;top:937px;width:214px">Sed ut perspiciatis unde omnis iste natus error sit voluptatem accusantium doloremque laudantium, totam rem aperiam, eaque ipsa quae ab illo</p>
  <div class="abs more" style="left:625px;top:987px">⊕ READ MORE</div>

  <div class="abs fan-logo" style="left:503px;top:1019px;color:var(--red)">Redport FC</div>
  <h3 class="abs item-title" style="left:625px;top:1016px;color:var(--blue)">Sed ut perspiciatis unde omn</h3>
  <p class="abs copy" style="left:625px;top:1038px;width:214px">Sed ut perspiciatis unde omnis iste natus error sit voluptatem accusantium doloremque laudantium, totam rem aperiam, eaque ipsa quae ab illo</p>
  <div class="abs more" style="left:625px;top:1088px">⊕ READ MORE</div>
</section>

<footer class="abs footer">
  <a class="abs social" style="left:130px" aria-label="Social link"></a>
  <a class="abs social" style="left:159px" aria-label="Social link"></a>
  <a class="abs social" style="left:188px" aria-label="Social link"></a>
  <a class="abs social" style="left:217px" aria-label="Social link"></a>
  <a class="abs social" style="left:246px" aria-label="Social link"></a>
  <p class="abs legal">© 2016 KickHarbor. All Copyrights are Reserved. Terms and Conditions And Privacy Policy</p>
</footer>
</body>
</html>
```